Home page concept, possible logo colour change

There is no need to code a home page, we are just looking for concept ideas.
We have had a logo designed for a new company we are starting named Corvantek Aluminium Windows & Doors. We are manufacturing bullet resistant window frames. We have had logo designed, we like the concept of the design, but the current colours (black and red) may not be the best option, especially when designing the website home page, and how it interacts with the logo colours. I have also attached the first draft of the home page which we are not happy with. The overall design/navigation is good, we have issues with the darkened out primary image and also the amount of red on the page, it just doesn't feel right. As mentioned before we are happy to look at colour changes to the logo.
Number of Pages Required
1 page
Look and feel
Each slider illustrates characteristics of the customer's brand and the style your logo design should communicate.

```html
<!DOCTYPE html>
<html lang="en">
<head>
<meta charset="utf-8">
<title>Corvantek Aluminium Windows &amp; Doors</title>
<link href="https://fonts.googleapis.com/css2?family=DM+Sans:wght@400;600&family=Roboto:wght@400;500;700&family=Roboto+Slab:wght@600;700&display=swap" rel="stylesheet">
<style>
  :root {
    --white: #ffffff;
    --ink: #1e2430;
    --nav-ink: #222833;
    --accent: #f08a2c;
    --accent-deep: #e4762a;
    --hero-top: #6e7a8c;
    --hero-mid: #7f8a99;
    --hero-warm: rgba(214, 168, 112, 0.35);
    --hero-bottom: #5f6b7e;
    --scrim: rgba(30, 38, 52, 0.42);
    --body-light: #f6f7f9;
  }
  * { margin: 0; padding: 0; box-sizing: border-box; }
  html, body { width: 1200px; height: 653px; overflow: hidden; background: var(--white); }
  .page { position: relative; width: 1200px; height: 653px; overflow: hidden; font-family: "Roboto", sans-serif; }

  .site-header { position: absolute; top: 0; left: 0; width: 1200px; height: 88px; background: var(--white); }
  .brand { position: absolute; left: 232px; top: 24px; color: var(--ink); font-weight: 700; }
  .brand-name { display: block; font-size: 27px; line-height: 28px; letter-spacing: -0.5px; }
  .brand-tagline { display: block; font-size: 6px; letter-spacing: 0.6px; text-transform: uppercase; margin-top: 1px; }

  .main-nav { position: absolute; top: 27px; left: 616px; display: flex; align-items: center; height: 29px; }
  .main-nav a { color: var(--nav-ink); text-decoration: none; font-size: 12px; font-weight: 500; margin-right: 19px; }
  .main-nav a.nav-cta { margin-right: 0; height: 29px; padding: 0 11px; display: flex; align-items: center; color: var(--white); font-weight: 700; background: var(--accent); border-radius: 0 15px 15px 0; }

  .hero { position: absolute; top: 88px; left: 0; width: 1200px; height: 565px; }
  .hero-photo { position: absolute; inset: 0; background:
      radial-gradient(ellipse 320px 230px at 600px 330px, var(--hero-warm), transparent 72%),
      linear-gradient(180deg, var(--hero-top) 0%, var(--hero-mid) 45%, var(--hero-bottom) 100%); }
  .hero-scrim { position: absolute; inset: 0; background: radial-gradient(ellipse 420px 300px at 600px 230px, var(--scrim), transparent 80%); }

  .hero-title, .hero-subtitle, .hero-text, .hero-button, .feature-icon, .feature-title, .feature-text { position: absolute; text-align: center; color: var(--white); }
  .hero-title { top: 96px; left: 0; width: 1200px; font-family: "Roboto Slab", Georgia, serif; font-weight: 700; font-size: 36px; line-height: 44px; letter-spacing: 0.3px; }
  .hero-subtitle { top: 172px; left: 0; width: 1200px; font-family: "Roboto Slab", Georgia, serif; font-weight: 600; font-size: 23px; line-height: 30px; color: var(--accent); text-shadow: 0 1px 3px rgba(20,26,36,0.45); }
  .hero-text { top: 206px; left: 420px; width: 360px; font-size: 12.5px; line-height: 18.7px; letter-spacing: 0.2px; color: var(--body-light); }
  .hero-button { top: 298px; left: 534px; width: 119px; height: 29px; display: flex; align-items: center; justify-content: center; font-weight: 700; font-size: 12px; text-decoration: none; background: var(--accent); }

  .feature-icon { display: block; }
  .feature-title { width: 220px; font-family: "DM Sans", sans-serif; font-weight: 600; font-size: 16px; line-height: 20px; color: var(--accent); letter-spacing: 0.5px; text-shadow: 0 1px 3px rgba(20,26,36,0.4); }
  .feature-text { width: 220px; font-family: "DM Sans", sans-serif; font-size: 9.5px; line-height: 18.6px; color: var(--body-light); }
</style>
</head>
<body>
<div class="page">
  <header class="site-header">
    <div class="brand">
      <span class="brand-name">Corvantek</span>
      <span class="brand-tagline">Aluminium Windows &amp; Doors</span>
    </div>
    <nav class="main-nav">
      <a href="#">Home</a>
      <a href="#">Our Products</a>
      <a href="#">Why Corvantek</a>
      <a href="#" class="nav-cta">Make an Enquiry</a>
    </nav>
  </header>

  <section class="hero">
    <div class="hero-photo" role="img" aria-label="Softly lit photograph of a grand glazed building entrance with revolving door and warm interior lighting"></div>
    <div class="hero-scrim"></div>

    <h1 class="hero-title">Bullet Resistant Windows &amp; Doors</h1>
    <h2 class="hero-subtitle">Your First Line of Defence</h2>
    <p class="hero-text">Lorem ipsum dolor sit amet, consectetur adipiscing elit, sed do eiusmod tempor incididunt ut labore et dolore magna aliqua. Quis ipsum suspendisse ultrices gravida. Risus com modo viverra maecenas accumsan lacus vel facilisis.</p>
    <a href="#" class="hero-button">Learn More</a>

    <svg class="feature-icon" style="left:362px;top:404px;" width="40" height="44" viewBox="0 0 42 46" fill="none" stroke="var(--accent)" stroke-width="2.4" stroke-linejoin="round">
      <path d="M21 2 L39 9 C39 26 32 38 21 44 C10 38 3 26 3 9 Z"/>
      <circle cx="21" cy="21" r="10"/>
      <path d="M21 6 V40 M5 21 H37"/>
    </svg>
    <div class="feature-title" style="left:271px;top:464px;">Premium Protection</div>
    <div class="feature-text" style="left:268px;top:492px;">Lorem ipsum dolor sit amet,<br>consectetur adipiscing elit.</div>

    <svg class="feature-icon" style="left:572px;top:401px;" width="51" height="49" viewBox="0 0 52 50" fill="none" stroke="var(--accent)" stroke-width="2.2" stroke-linejoin="round">
      <path d="M2 2 L50 12 V40 L2 48 Z"/>
      <path d="M14 4.5 V46 M26 7 V44 M38 9.5 V42 M2 18 L50 22 M2 34 L50 32"/>
      <path d="M30 44 L50 44"/>
    </svg>
    <div class="feature-title" style="left:490px;top:462px;">Aesthetic Design</div>
    <div class="feature-text" style="left:490px;top:492px;">Lorem ipsum dolor sit amet,<br>consectetur eiusmod.</div>

    <svg class="feature-icon" style="left:811px;top:411px;" width="52" height="41" viewBox="0 0 52 42" fill="none" stroke="var(--accent)" stroke-width="2.4" stroke-linejoin="round" stroke-linecap="round">
      <rect x="2" y="2" width="34" height="38" rx="1"/>
      <path d="M13 2 V13 H25 V2"/>
      <path d="M38 12 H50 M40 22 H50 M38 32 H46"/>
    </svg>
    <div class="feature-title" style="left:723px;top:462px;">Prompt Delivery</div>
    <div class="feature-text" style="left:722px;top:492px;">Lorem ipsum dolor sit amet,<br>con elit, sed do eiusmod.</div>
  </section>
</div>
</body>
</html>
```